Thistlewood Group Business Card Design

We are looking for a new business card design, we are not happy with our current design. We are a boutique management consulting firm and our clients are typically meridian 400 companies.

I have attached the current front and back that we have as well as a version of our logo that can be used. I am trying to get a higher resolution version of the logo file to upload to the project.

Target Market(s)

Meridian 400 companies are our primary client base. Financial services, life sciences, pharmaceuticals and telecom companies are

Industry/Entity Type

Management Consulting

Contact Information for Business Card

We are trying to communicate a high degree of professionalism, a somewhat minimalist perhaps with some air of whimsy (without overdoing it). Attached is the current design, front and back as well as logos. I like the current back of the card and assume we will keep the phrase the same.

From a color palette perspective, I prefer to stay with a gray scale as they are today.

Font styles to use
Sans Serif

Colors
1b1b1b
474747
ffffff

Requirements
Must have
• Two sided business card design. File format should be something that can be used outside of Photoshop like MS Publisher so that they can be edited with personal information.
• Font should be calibri or something very similar and should be available within MS Office
Should not have
• No other logos or graphics outside of the logo provided.

```html
<!DOCTYPE html>
<html lang="en">
<head>
<meta charset="utf-8">
<title>Thistlewood Group Business Card</title>
<link href="https://fonts.googleapis.com/css2?family=Montserrat:wght@300;400;600;700&display=swap" rel="stylesheet">
<style>
  :root {
    --card: #1b1b1b;
    --mid: #474747;
    --ink: #ffffff;
    --backdrop: #d9d9d9;
  }
  * { box-sizing: border-box; margin: 0; padding: 0; }
  html, body {
    width: 1200px; height: 900px; overflow: hidden;
    background: var(--backdrop);
    font-family: "Montserrat", sans-serif;
    color: var(--ink);
  }
  .canvas { position: relative; width: 1200px; height: 900px; }
  .card {
    position: absolute;
    width: 620px; height: 354px;
    left: 290px;
    background: var(--card);
    border-radius: 22px;
    overflow: hidden;
  }
  .card-front { top: 58px; }
  .card-back { top: 488px; }

  /* front */
  .front-brand {
    position: absolute; top: 92px; left: 0; right: 0;
    display: flex; align-items: center; justify-content: center; gap: 14px;
  }
  .brand-dot { width: 34px; height: 34px; border-radius: 50%; background: var(--ink); }
  .brand-name { font-weight: 600; font-size: 60px; letter-spacing: -0.5px; line-height: 1; }
  .brand-name sup { font-size: 12px; font-weight: 400; vertical-align: 44px; margin-left: 2px; }
  .tagline { position: absolute; top: 196px; left: 0; right: 0; text-align: center; }
  .tagline-lead { font-weight: 700; font-size: 16px; letter-spacing: 7px; }
  .tagline-rest { font-weight: 300; font-size: 19px; letter-spacing: 1px; margin-top: 4px; }
  .front-url { font-size: 12px; margin-top: 12px; font-weight: 400; }
  .front-url b { font-weight: 700; }

  /* back */
  .back-info { position: absolute; left: 46px; top: 40px; }
  .back-brand { display: flex; align-items: center; gap: 9px; }
  .back-brand .brand-dot { width: 18px; height: 18px; }
  .back-brand .brand-name { font-size: 32px; }
  .back-brand .brand-name sup { font-size: 8px; vertical-align: 24px; }
  .person-name { font-weight: 700; font-size: 21px; margin-top: 8px; }
  .person-role { font-weight: 300; font-size: 14px; line-height: 1.3; }
  .contact-list { list-style: none; margin-top: 6px; }
  .contact-list li { display: flex; align-items: center; gap: 9px; font-size: 14px; font-weight: 300; line-height: 1.45; }
  .contact-list b { font-weight: 700; }
  .contact-icon { width: 11px; height: 11px; fill: none; stroke: var(--ink); stroke-width: 1.6; }
  .office-name { font-weight: 700; font-size: 17px; margin-top: 8px; }
  .office-lines { font-weight: 300; font-size: 14px; line-height: 1.3; }
  .back-mark {
    position: absolute; right: 70px; top: 58px;
    width: 170px; height: 170px; border-radius: 50%;
    background: var(--ink);
  }
</style>
</head>
<body>
<main class="canvas">
  <section class="card card-front" aria-label="Card front">
    <div class="front-brand">
      <span class="brand-dot"></span>
      <span class="brand-name">Thistlewood<sup>™</sup></span>
    </div>
    <div class="tagline">
      <p class="tagline-lead">THE PREFERRED CHOICE</p>
      <p class="tagline-rest">FOR LEADERSHIP’S TOP PRIORITIES</p>
      <p class="front-url">www.<b>thistlewoodgroup</b>.com</p>
    </div>
  </section>

  <section class="card card-back" aria-label="Card back">
    <div class="back-info">
      <div class="back-brand">
        <span class="brand-dot"></span>
        <span class="brand-name">Thistlewood<sup>™</sup></span>
      </div>
      <p class="person-name">Owen Hartley</p>
      <p class="person-role">Los Angeles Office<br>Managing Director</p>
      <ul class="contact-list">
        <li><svg class="contact-icon" viewBox="0 0 12 12"><path d="M2 1.5 L4 1.5 L5 4 L3.8 5 Q5 7.3 7 8.2 L8 7 L10.5 8 L10.5 10 Q6 10.5 3.5 7.5 Q1.5 5 2 1.5 Z"/></svg>555.014.2270</li>
        <li><svg class="contact-icon" viewBox="0 0 12 12"><rect x="1" y="2.5" width="10" height="7"/><path d="M1 2.5 L6 6.5 L11 2.5"/></svg>ohartley@thistlewoodgroup.com</li>
        <li><svg class="contact-icon" viewBox="0 0 12 12"><circle cx="6" cy="6" r="5"/><ellipse cx="6" cy="6" rx="2.2" ry="5"/><path d="M1 6 H11"/></svg>www.<b>thistlewoodgroup</b>.com</li>
      </ul>
      <p class="office-name">Thistlewood Group, Inc.</p>
      <p class="office-lines">Headquarters<br>218 Larkspur Avenue<br>Suite 104<br>Harbor Point, WA 98000</p>
    </div>
    <div class="back-mark" aria-hidden="true"></div>
  </section>
</main>
</body>
</html>
```